Wordpress Design Project - IT Consulting Services Web Site

Our are starting a new technology services company. We will provide services in software implementation and business intelligence.

We need a beautiful Wordpress web site design. We need a design for the homepage, and one interior content page.

The site must have a very professional and polished look and feel. What I have suggested below are things that I think work, but I am not a designer and I am open to your professional opinions. Please be willing to use your best judgment.

The homepage should have the following elements:
- A Header Area that includes:
o The company logo, and
o navigation (consistent with the interior page)
o a social media link section that includes rss feeds, youtube, facebook, linkedin and tweets
- A Body that includes:
o A slider
o An area that features up to six of the most recent or important posts including a thumbnail and small picture, a title, and a short excerpt for each.
o An area for around 100 words of text and an image
- A footer that includes:
o The company logo
o Contact information

The interior page is relatively simple. It should include the same navigation element as the homepage, and accommodate a one column text layout.

The current site …
You can visit the current site at www.korvelpath.com I built the current site using the “Velthor Quick Pane” premium theme. If you visit this site you get a sense of some of the things I am talking about, but there are things that I do not like about the current site. Here’s what I like and what I don’t like.

What I like about the current site:
- It is reactive – it adapts to the size of the viewing browser
- It has a “metro” feel to it. The company will have an association with Microsoft and having a “metro” theme is a plus, but not a requirement.
- It is different without being hard to navigate – the site the slider is from the “glide cascade widget”, the posts are represented with tiles and rearrange themselves when a topic is selected.

What I don’t like:
- The site lacks a cohesive feel – it feels to me like a bunch of different elements without a single theme that pulls everything together.
- It is not aesthetically appealing to me.
- The tiles in the post section are too big.
- I don’t like the white background – I would prefer a background color and ideally a background that somehow incorporates the graphic in the logo.

About themes
As I said, I used a Velthor theme in my design. I will be happy to continue using this theme, or would be willing to buy a new premium theme, so long as the cost is less than $100 U.S.

Site Map:
What we do
ERP Implementation
Business Intelligence
Who we are
What’s different about us
Principles
Mission, Vision, Values
Actions
How we work
What’s Different About Us
Blogs
What Papers
Presentations
Join
What we are looking for
What are you looking for?
Benefits
Context
Updates

Regarding Pictures
Please do not feel you need to use any of the pictures currently on the site.  Use whatever pictures you feel look best.  Comps are okay. 

It is not necessary to use any of the content on the current site - you do not need to use either the pictures or the text.  Please feel free to use pictures of your choice (comps okay), and/or lorem text.

The top level navigation is the navigation I would like.

Hello all,

Since this is a Wordpress project, it goes without saying I will need to implement this design in Wordpress.  It is not absolutely necessary that a design that matches an existing template (free or not), but a design that does will have an advantage over a design which requires that a new template be coded from scratch.

Thank you.

Target Market(s)

Business executives and potential employees

Industry/Entity Type

Software

Requirements
Nice to have
• It would be nice if the site was reactive.

```html
<!DOCTYPE html>
<html lang="en">
<head>
<meta charset="utf-8">
<title>KorvelPath – IT Consulting</title>
<link href="https://fonts.googleapis.com/css2?family=Kreon:wght@400&family=Noto+Sans:wght@400;500&display=swap" rel="stylesheet">
<style>
  :root {
    --blue: #0a93d3;
    --blue-light: #19a6e6;
    --slate: #4a5059;
    --navy: #1d2a3a;
    --black: #050505;
    --white: #ffffff;
    --text-soft: #e6e8ea;
    --gold: #e0a21a;
  }
  * { margin: 0; padding: 0; box-sizing: border-box; }
  html, body { width: 938px; height: 1200px; overflow: hidden; }
  body { font-family: "Noto Sans", Verdana, sans-serif; background: var(--slate); color: var(--white); position: relative; }

  .hero { position: absolute; left: 0; top: 0; width: 938px; height: 333px;
    background: linear-gradient(100deg, #d7d9dc 0%, #b7bcc2 25%, #d4d0cb 45%, #eaeaea 62%, #9ea7b3 80%, #d8c9b7 100%); }
  .hero-photo { position: absolute; inset: 0; }
  .site-header { position: absolute; left: 0; top: 0; width: 938px; height: 73px; background: rgba(40,44,50,.72); }
  .brand { position: absolute; left: 120px; top: 44px; display: flex; align-items: center; gap: 8px;
    font-size: 22px; font-weight: 400; color: var(--white); letter-spacing: -0.5px; }
  .brand-dot { width: 14px; height: 14px; border-radius: 50%; background: var(--blue); }
  .main-nav { position: absolute; right: 29px; top: 40px; display: flex; gap: 20px; }
  .main-nav a { font-size: 12.5px; color: var(--white); text-decoration: none; padding: 2px 7px; line-height: 16px; }
  .main-nav a.active { background: var(--blue); }

  .slide-title { position: absolute; left: 686px; top: 126px; width: 174px; height: 52px; background: var(--black);
    font-family: "Kreon", Georgia, serif; font-size: 25px; color: var(--white); line-height: 52px; text-align: center; letter-spacing: .5px; }
  .slide-caption { position: absolute; left: 553px; top: 237px; width: 385px; height: 53px; background: var(--black);
    font-family: "Kreon", Georgia, serif; font-size: 20px; line-height: 53px; padding-left: 33px; letter-spacing: .5px; }
  .slide-prev { position: absolute; left: 539px; top: 237px; }
  .slide-sub { position: absolute; left: 586px; top: 293px; width: 352px; height: 18px; background: var(--black);
    font-family: "Kreon", Georgia, serif; font-size: 13.5px; line-height: 18px; padding-left: 16px; letter-spacing: .4px; }

  .join-band { position: absolute; left: 0; top: 333px; width: 938px; height: 53px; background: var(--blue); border-top: 2px solid #d9e7ee; }
  .join-band p { position: absolute; left: 109px; top: 12px; font-size: 13.5px; line-height: 13px; letter-spacing: .3px; }
  .join-btn { position: absolute; left: 611px; top: 14px; width: 139px; height: 24px; background: var(--white); color: #1b1b1b;
    font-size: 13.5px; letter-spacing: 1.5px; text-align: center; line-height: 25px; }

  .posts { position: absolute; left: 0; top: 386px; width: 938px; height: 509px; background: var(--slate); }
  .post { position: absolute; width: 228px; }
  .post-thumb { position: relative; width: 228px; height: 123px; border: 2px solid var(--blue); }
  .post-thumb .fill { position: absolute; inset: 2px; }
  .read-more { position: absolute; left: -6px; bottom: 8px; background: var(--blue); font-size: 9.5px; padding: 3px 6px; letter-spacing: .3px; }
  .post h3 { font-weight: 400; font-size: 13px; color: var(--blue-light); margin: 14px 0 3px 4px; letter-spacing: .3px; }
  .post p { font-size: 9.8px; line-height: 12.8px; color: var(--text-soft); margin-left: 4px; letter-spacing: .25px; }

  .people-first { position: absolute; left: 0; top: 895px; width: 938px; height: 191px; background: var(--navy); }
  .people-first h2 { position: absolute; left: 112px; top: 40px; font-size: 16px; font-weight: 400; letter-spacing: .3px; }
  .people-first p { position: absolute; left: 112px; top: 70px; width: 440px; font-size: 11.2px; line-height: 12.8px; color: var(--blue-light); letter-spacing: .3px; }
  .people-first .more { position: absolute; left: 486px; top: 118px; font-size: 9.8px; letter-spacing: .5px; }
  .portrait { position: absolute; left: 617px; top: 9px; width: 172px; height: 172px; border-radius: 50%; border: 3px solid var(--blue);
    background: radial-gradient(circle at 55% 45%, #c9a98d 0%, #8a7a6e 40%, #4c5360 80%, #2c3440 100%); }

  .site-footer { position: absolute; left: 0; top: 1086px; width: 938px; height: 114px; background: var(--slate); }
  .site-footer .brand { left: 111px; top: 56px; }
  .contact-label { position: absolute; left: 358px; top: 25px; background: var(--blue); font-size: 9.8px; padding: 2px 4px; letter-spacing: .3px; }
  .contact-box { position: absolute; left: 358px; top: 44px; width: 282px; height: 35px; background: var(--blue);
    font-size: 9.8px; line-height: 12.5px; padding: 6px 7px; overflow: hidden; letter-spacing: .2px; }
  .social { position: absolute; left: 704px; top: 58px; display: flex; gap: 8px; }
  .social span { width: 22px; height: 22px; border-radius: 50%; background: #2a2a2a; border: 2px solid var(--gold); }
</style>
</head>
<body>
  <section class="hero">
    <div class="hero-photo" role="img" aria-label="Office team of colleagues reviewing documents together, softly blurred background"></div>
    <header class="site-header">
      <div class="brand"><span>KorvelPath</span><span class="brand-dot"></span></div>
      <nav class="main-nav">
        <a class="active" href="#">OUR SERVICES</a>
        <a href="#">ABOUT US</a>
        <a href="#">HOW WE WORK</a>
        <a href="#">JOIN</a>
        <a href="#">CONTACT</a>
      </nav>
    </header>
    <div class="slide-title">Lorem Ipsum</div>
    <svg class="slide-prev" width="40" height="53" viewBox="0 0 40 53" aria-hidden="true">
      <polygon points="14,0 40,0 40,53 0,53" fill="#050505"/>
      <polygon points="14,0 30,53 0,53 0,28" fill="#0a93d3"/>
      <polyline points="15,21 9,28 15,35" fill="none" stroke="#fff" stroke-width="2"/>
    </svg>
    <div class="slide-caption">Lorem Ipsum is simply dummy text</div>
    <div class="slide-sub">Lorem Ipsum is simply dummy text</div>
  </section>

  <section class="join-band">
    <p>Lorem Ipsum is simply dummy text of the printing<br>and typesetting industry.</p>
    <div class="join-btn">JOIN US</div>
  </section>

  <section class="posts">
    <article class="post" style="left:109px;top:38px">
      <div class="post-thumb"><div class="fill" role="img" aria-label="Close-up of a green plant with budding berries" style="background:radial-gradient(circle at 40% 50%,#9acb3c,#3f7a1c 55%,#1a3a0e)"></div><span class="read-more">READ MORE</span></div>
      <h3>Growth</h3>
      <p>Lorem Ipsum is simply dummy text of the printing and typesetting industry. Lorem Ipsum has been the industry's standard dummy text ever since the 1500s.</p>
    </article>
    <article class="post" style="left:349px;top:38px">
      <div class="post-thumb"><div class="fill" role="img" aria-label="Black and white chess pieces on a board" style="background:linear-gradient(180deg,#1a1a1a,#6b6b6b 70%,#2a2a2a)"></div><span class="read-more">READ MORE</span></div>
      <h3>ERP Implementations</h3>
      <p>Lorem Ipsum is simply dummy text of the printing and typesetting industry. Lorem Ipsum has been the industry's standard dummy text ever since the 1500s.</p>
    </article>
    <article class="post" style="left:589px;top:38px">
      <div class="post-thumb"><div class="fill" role="img" aria-label="Hand touching a glowing circular digital interface" style="background:radial-gradient(circle at 35% 30%,#8a8a8a,#2c2c2c 45%,#121212)"></div><span class="read-more">READ MORE</span></div>
      <h3>Business Intelligence</h3>
      <p>Lorem Ipsum is simply dummy text of the printing and typesetting industry. Lorem Ipsum has been the industry's standard dummy text ever since the 1500s.</p>
    </article>
    <article class="post" style="left:109px;top:275px">
      <div class="post-thumb"><div class="fill" role="img" aria-label="Child standing on an open road under a blue sky" style="background:linear-gradient(180deg,#6ea6d8 0%,#bcd3e6 35%,#a79c7e 45%,#857a66 100%)"></div><span class="read-more">READ MORE</span></div>
      <h3>Respect The Journey</h3>
      <p>Lorem Ipsum is simply dummy text of the printing and typesetting industry. Lorem Ipsum has been the industry's standard dummy text ever since the 1500s.</p>
    </article>
    <article class="post" style="left:349px;top:275px">
      <div class="post-thumb"><div class="fill" role="img" aria-label="Business handshake over a desk, black and white" style="background:linear-gradient(135deg,#e8e8e8,#9a9a9a 45%,#2a2a2a 75%,#d0d0d0)"></div><span class="read-more">READ MORE</span></div>
      <h3>What's The Idea?</h3>
      <p>Lorem Ipsum is simply dummy text of the printing and typesetting industry. Lorem Ipsum has been the industry's standard dummy text ever since the 1500s.</p>
    </article>
    <article class="post" style="left:589px;top:275px">
      <div class="post-thumb"><div class="fill" role="img" aria-label="Team of business people in a meeting around a laptop" style="background:linear-gradient(120deg,#d6dbe1,#8d97a4 45%,#3c4350 75%,#c9b7a4)"></div><span class="read-more">READ MORE</span></div>
      <h3>How it Works.</h3>
      <p>Lorem Ipsum is simply dummy text of the printing and typesetting industry. Lorem Ipsum has been the industry's standard dummy text ever since the 1500s.</p>
    </article>
  </section>

  <section class="people-first">
    <h2>Putting People First</h2>
    <p>Every services firm is made up of people, processes and tools. At Korvel Path, we put people first, tailoring everything we do to find, hire, train, and keep the very best people. Because once you have the best people everything else follows.</p>
    <span class="more">READ MORE</span>
    <div class="portrait" role="img" aria-label="Portrait of a smiling consultant in an office"></div>
  </section>

  <footer class="site-footer">
    <div class="brand"><span>KorvelPath</span><span class="brand-dot"></span></div>
    <span class="contact-label">CONTACT US</span>
    <div class="contact-box">Lorem Ipsum is simply dummy text of the printing and typesetting industry. Lorem Ipsum has been the</div>
    <div class="social" aria-label="Social links"><span></span><span></span><span></span><span></span></div>
  </footer>
</body>
</html>
```